Website for boutique digital agency helping high-tech startups accelerate growth.

We need a website design for a relatively young company based in Mauritius called 'LoomTrax'.

We are a professional services firm delivering digital infrastructure for revenue operations (RevOps)*.

Entrepreneurial startups and SMBs in the technology sector work with us to accelerate growth by delivering extraordinary customer experiences across the full customer lifecycle.

We would like a colourful design that utilises the (4) colours of our existing logo design.

The final design should communicate dynamic growth through relentless customer focus.
----------------------------------------------------------
*Revenue Operations (RevOps) is the strategic alignment of sales, marketing and customer success operations to accelerate growth by delivering extraordinary customer experiences across the full customer life cycle.
Updates

Target Market(s)

Entrepreneurial startups and SMBs (Small/Medium Businesses) in the technology sector.

Question: Why the technology sector?

Answer: Because technology entrepreneurs often have a tremendous challenge to effectively communicate to the market and to prospective customers the value and the benefits of their products & services due to the inherent complexity of technological innovation.

LoomTrax is a team of creatively-minded engineers and technologists who have worked with and understand the technologies and innovations our clients are passionate about bringing to market.

Industry/Entity Type

Professional Service

Number of Pages Required

5+ page

Font styles to use
Sans Serif

Requirements
Must have
• Minimalistic designs rich with visual meaning are highly preferred. Mobile responsive designs are also required. Must show how designs render on Desktop, Tablet and Smartphone devices.

Website pages:
1) Homepage: problem statement, target customers, value proposition & benefits
2) Services: 3-4 tiers of services packages with pricing and "how to work with us"
3) Resources: links to all kinds of relevant materials
4) Contact Us: contact form and special project quote form
5) Blog: matrix design with featured images for each post
Nice to have
• Bold, interesting, colourful, inspiring images that visually communicate:
- relentless customer focus
- extraordinary, memorable experiences
- business at the speed of innovation
Should not have
• Any meme or theme that panders to "political correctness".

```html
<!DOCTYPE html>
<html lang="en">
<head>
<meta charset="utf-8">
<title>LoomTrax — Digital infrastructure for revenue operations</title>
<link href="https://fonts.googleapis.com/css2?family=Inter:wght@800;900&family=DM+Sans:wght@400;500;700&display=swap" rel="stylesheet">
<style>
  :root {
    --bg: #1a1a1a;
    --ink: #ffffff;
    --ink-dark: #111111;
    --line: #3a3a3a;
    --coral: #ff5a4e;
    --amber: #ffb627;
    --teal: #19c3b1;
    --violet: #7b6cf0;
  }
  * { box-sizing: border-box; margin: 0; padding: 0; }
  html, body { width: 1200px; height: 807px; overflow: hidden; background: var(--bg); }
  body { font-family: "DM Sans", Arial, sans-serif; color: var(--ink); }

  .hero { position: relative; width: 1200px; height: 807px; background: var(--bg); }

  .brand {
    position: absolute; left: 30px; top: 38px;
    display: flex; align-items: center; gap: 8px;
    font-family: "DM Sans", Arial, sans-serif; font-weight: 700; font-size: 18px;
    color: var(--ink); text-decoration: none; letter-spacing: -0.01em;
  }
  .brand-dot { width: 11px; height: 11px; background: var(--coral); }

  .btn {
    display: inline-flex; align-items: center; justify-content: center;
    background: var(--ink); color: var(--ink-dark);
    font-family: "DM Sans", Arial, sans-serif; font-weight: 700; font-size: 8px;
    text-transform: uppercase; letter-spacing: 0.01em; text-decoration: none;
    width: 87px; height: 29px;
  }
  .btn-talk { position: absolute; left: 1081px; top: 33px; background: var(--coral); color: var(--ink); }
  .btn-services { position: absolute; left: 250px; top: 541px; background: var(--amber); }

  .menu-toggle { position: absolute; left: 35px; top: 396px; width: 22px; height: 12px; }
  .menu-toggle span { display: block; height: 2px; background: var(--ink); margin-bottom: 6px; }
  .menu-toggle span:last-child { background: var(--teal); }

  .headline {
    position: absolute; left: 243px; top: 162px;
    font-family: "Inter", Arial, sans-serif; font-weight: 900;
    font-size: 77px; line-height: 92px; letter-spacing: -0.055em;
    color: var(--ink); white-space: nowrap;
  }
  .headline-stop { color: var(--teal); }

  .intro {
    position: absolute; left: 248px; top: 459px; width: 200px;
    font-size: 9px; line-height: 17px; font-weight: 500;
  }

  .slider-nav { position: absolute; left: 250px; top: 594px; display: flex; gap: 12px; }
  .slider-btn {
    width: 37px; height: 37px; border: 1px solid var(--line); border-radius: 50%;
    display: flex; align-items: center; justify-content: center;
  }
  .slider-btn--next { border-color: var(--violet); }

  .contact-email {
    position: absolute; left: 38px; top: 770px;
    transform: rotate(-90deg); transform-origin: left top;
    font-size: 10px; font-weight: 500; white-space: nowrap; color: var(--ink);
    text-decoration: none;
  }

  .social {
    position: absolute; left: 1150px; top: 279px;
    list-style: none; display: flex; flex-direction: column; gap: 24px;
  }
  .social a {
    display: block; writing-mode: vertical-rl;
    font-size: 8px; font-weight: 700; color: var(--ink); text-decoration: none;
  }

  .scroll-cue { position: absolute; left: 1152px; top: 764px; }

  .progress { position: absolute; left: 0; bottom: 0; width: 1200px; height: 6px; display: flex; }
  .progress span { flex: 1; }
  .progress .p-coral { background: var(--coral); }
  .progress .p-amber { background: var(--amber); }
  .progress .p-teal { background: var(--teal); }
  .progress .p-violet { background: var(--violet); }
</style>
</head>
<body>
<main class="hero">
  <a class="brand" href="#"><span class="brand-dot"></span>LoomTrax</a>
  <a class="btn btn-talk" href="#">Let’s talk</a>

  <div class="menu-toggle" aria-label="Menu"><span></span><span></span></div>

  <h1 class="headline">We deliver digital<br>infrastructure for<br>revenue operations<span class="headline-stop">.</span></h1>

  <p class="intro">Entrepreneurial startups and SMBs in the technology sector work with us to accelerate growth by delivering extraordinary customer experiences across the full customer lifecycle.</p>

  <a class="btn btn-services" href="#">See what we do</a>

  <div class="slider-nav">
    <div class="slider-btn" aria-label="Previous">
      <svg width="9" height="7" viewBox="0 0 9 7"><path d="M0 3.5 L4 0 V2.3 H9 V4.7 H4 V7 Z" fill="#fff"/></svg>
    </div>
    <div class="slider-btn slider-btn--next" aria-label="Next">
      <svg width="9" height="7" viewBox="0 0 9 7"><path d="M9 3.5 L5 0 V2.3 H0 V4.7 H5 V7 Z" fill="#7b6cf0"/></svg>
    </div>
  </div>

  <a class="contact-email" href="#">hello@loomtrax.io</a>

  <ul class="social">
    <li><a href="#">kitestream</a></li>
    <li><a href="#">murmur</a></li>
    <li><a href="#">lenscape</a></li>
    <li><a href="#">reelbox</a></li>
    <li><a href="#">proflink</a></li>
  </ul>

  <svg class="scroll-cue" width="7" height="10" viewBox="0 0 7 10" aria-label="Scroll down">
    <path d="M2.3 0 H4.7 V5 H7 L3.5 10 L0 5 H2.3 Z" fill="#19c3b1"/>
  </svg>

  <div class="progress"><span class="p-coral"></span><span class="p-amber"></span><span class="p-teal"></span><span class="p-violet"></span></div>
</main>
</body>
</html>
```